Corvalink_DLX Framework Materials

I need to take existing documents, presentations, and tools and rebrand them under a different company name and image. I will attach the companies logo and templates that I need you to use. The copy must be editable and in PDF and Powerpoint formats. I sell a sales program that teaches a method of consulting that requires an Opportunity Assessment document that is used as a customer deliverable during the sales process. I need to use the same copy from the assessment I attached for Harbor Fable, but change the brand to match my client's company and convert it into a Powerpoint with my clients brand.

Target Market(s)

Business Technology Consulting

Industry/Entity Type

Information Technology

Font styles to use
Serif

Colors
ec1f27
000000
5c5c5c
ffffff

Requirements
Must have
• Same color and theme and the company logo and website www.corvalink-example.com
Nice to have
• Some font choices and ability to add and delete sections of the document similar to my Word document.

```html
<!DOCTYPE html>
<html lang="en">
<head>
<meta charset="utf-8">
<title>Executive Summary – Corvalink</title>
<link rel="stylesheet" href="https://fonts.googleapis.com/css2?family=Montserrat:wght@400;600;700;800&display=swap">
<style>
  :root {
    --brand-red: #d00000;
    --accent-red: #ec1f27;
    --ink: #000000;
    --body-grey: #333333;
    --bullet-grey: #4a4a4a;
    --band-grey: #8a8a8a;
    --paper: #ffffff;
  }
  * { box-sizing: border-box; margin: 0; padding: 0; }
  html, body {
    width: 1200px;
    height: 900px;
    overflow: hidden;
    background: var(--paper);
  }
  .slide {
    position: relative;
    width: 1200px;
    height: 900px;
    background: var(--paper);
    font-family: "Montserrat", Arial, sans-serif;
    overflow: hidden;
  }
  .header-bands,
  .footer-bands {
    position: absolute;
    left: 0;
    display: block;
  }
  .header-bands { top: 0; }
  .footer-bands { bottom: 0; }
  .slide-title {
    position: absolute;
    left: 24px;
    top: 26px;
    color: var(--paper);
    font-size: 37px;
    font-weight: 700;
    letter-spacing: 0.5px;
    line-height: 1;
  }
  .brand-name {
    position: absolute;
    right: 30px;
    top: 22px;
    display: flex;
    align-items: center;
    gap: 12px;
    color: var(--paper);
    font-size: 34px;
    font-weight: 600;
    letter-spacing: 3px;
    line-height: 1;
  }
  .brand-name .brand-dot {
    width: 16px;
    height: 16px;
    background: var(--paper);
    border-radius: 50%;
  }
  .section-title {
    color: var(--brand-red);
    font-size: 31px;
    font-weight: 800;
    line-height: 1;
    letter-spacing: 0.3px;
  }
  .intro {
    position: absolute;
    left: 22px;
    top: 138px;
    width: 1164px;
  }
  .intro-text {
    margin-top: 10px;
    color: var(--body-grey);
    font-size: 16.6px;
    line-height: 29.5px;
    text-align: justify;
  }
  .intro-text + .intro-text { margin-top: 29.5px; }
  .goals {
    position: absolute;
    left: 22px;
    top: 483px;
    width: 1100px;
  }
  .goal-list {
    list-style: none;
    margin-top: 30px;
    padding-left: 45px;
  }
  .goal-list li {
    position: relative;
    padding-left: 46px;
    color: var(--bullet-grey);
    font-size: 21px;
    line-height: 30px;
    margin-bottom: 19.5px;
  }
  .goal-list li::before {
    content: "";
    position: absolute;
    left: 2px;
    top: 6px;
    width: 17px;
    height: 17px;
    background: var(--brand-red);
    transform: rotate(45deg);
  }
  .page-number {
    position: absolute;
    right: 18px;
    bottom: 12px;
    width: 68px;
    height: 68px;
  }
  .page-number svg { display: block; }
  .page-number span {
    position: absolute;
    inset: 0;
    display: flex;
    align-items: center;
    justify-content: center;
    color: var(--paper);
    font-size: 24px;
    font-weight: 800;
  }
</style>
</head>
<body>
<main class="slide">
  <svg class="header-bands" width="1200" height="104" viewBox="0 0 1200 104" aria-hidden="true">
    <rect x="0" y="0" width="1200" height="88" fill="var(--brand-red)"/>
    <polygon points="436,88 1200,88 1200,103 420,103" fill="var(--ink)"/>
  </svg>
  <h1 class="slide-title">EXECUTIVE SUMMARY</h1>
  <div class="brand-name"><span class="brand-dot"></span>CORVALINK</div>

  <section class="intro">
    <h2 class="section-title">SUBTEXT TITLE HERE</h2>
    <p class="intro-text">We appreciate the opportunity to assist with identifying solutions for unified communications &amp; collaboration platforms. Based on the information gathered in the first meeting we&nbsp; have developed several potential solutions that can support your business requirements and align with your success criteria&nbsp; .</p>
    <p class="intro-text">The following proposal includes options to partner with Relaynet and leverage our portfolio of UCaaS service providers that meet the needs of your organization. As part of the partnership we can provide evaluations from multiple service providers and assist in making the recommendation based on past experience and expertise with UCaaS platforms. Solutions outlined in this proposal are delivered by leading service providers that Relaynet has partnerships established, and Harbor Fable will have a direct relationship with the actual service provider.</p>
  </section>

  <section class="goals">
    <h2 class="section-title">BULLET TITLE HERE</h2>
    <ul class="goal-list">
      <li>Gain confirmation that we have identified all the issues and requirements we discussed</li>
      <li>Ensure we have a clear understanding of the business objectives and expected outcomes</li>
      <li>Understand the decision-making criteria</li>
      <li>Review potential solutions and determine the best path</li>
      <li>Begin service provider engagement process</li>
    </ul>
  </section>

  <svg class="footer-bands" width="1200" height="42" viewBox="0 0 1200 42" aria-hidden="true">
    <rect x="0" y="2" width="1200" height="40" fill="var(--ink)"/>
    <polygon points="800,0 1200,0 1200,42 772,42" fill="var(--band-grey)"/>
    <polygon points="0,24 760,24 740,42 0,42" fill="var(--ink)"/>
  </svg>
  <div class="page-number">
    <svg width="68" height="68" viewBox="0 0 68 68" aria-hidden="true">
      <polygon points="34,2 66,34 34,66 2,34" fill="var(--brand-red)" stroke="var(--paper)" stroke-width="3"/>
    </svg>
    <span>1</span>
  </div>
</main>
</body>
</html>
```